Vorimelo Mobile App

We are in need of a design for a mobile application that delivers relevant content to users based on the profile that they enter and based on the answers that they enter in a daily health tracker. There also will be functionality that will allow a user to check the cost of a medical service/ procedure before going to the medical provider (could get a list of providers and costs after entering procedure, service or prescription in a search box). The content will be articles or information that our team will find/develop on a daily basis and put into a database that the app will pull off of. The profile needs to capture age, sex, ethinicity (optional) and then have a list of topics that the user can select to get daily updated information/content. These topics are: Diabetes, Heart Disease, Hypertension, COPD, Back Pain, Weight Management, Depression, Cancer, Wellness Plan. The final design should allow for users to receive helpful health care information every day based on their profile and the answers in the daily health tracker.

Medical

```html
<!DOCTYPE html>
<html lang="en">
<head>
<meta charset="utf-8">
<title>Vorimelo Feed</title>
<link rel="stylesheet" href="https://fonts.googleapis.com/css2?family=Roboto+Condensed:wght@300;400&family=Roboto:wght@300;400;900&display=swap">
<style>
  :root {
    --brand-green: #4bbd63;
    --screen-bg: #e8e8e8;
    --card-bg: #ffffff;
    --card-border: #d9d9d9;
    --title-ink: #111111;
    --body-ink: #9a9a9a;
    --heart-red: #d8282c;
    --xray-orange: #fb9a06;
    --health-lime: #7dcf2f;
    --services-blue: #2f8fd5;
    --tab-ink: #8e8e8e;
    --tab-active: #4bbd63;
    --white: #ffffff;
  }
  * { box-sizing: border-box; margin: 0; padding: 0; }
  html, body { width: 676px; height: 1200px; overflow: hidden; background: var(--screen-bg); }
  .screen {
    position: relative; width: 640px; height: 1136px;
    transform: scale(1.05625); transform-origin: 0 0;
    background: var(--screen-bg); overflow: hidden;
    font-family: "Roboto", sans-serif;
  }
  .app-header {
    position: absolute; left: 0; top: 0; width: 640px; height: 128px;
    background: var(--brand-green); color: var(--white);
  }
  .status-bar { position: absolute; left: 0; top: 0; width: 640px; height: 40px; font-size: 22px; font-weight: 400; }
  .status-carrier { position: absolute; left: 12px; top: 7px; display: flex; align-items: center; gap: 6px; }
  .signal { display: flex; gap: 2px; }
  .signal span { width: 10px; height: 10px; border-radius: 50%; border: 1.5px solid var(--white); }
  .signal span.on { background: var(--white); }
  .wifi { position: absolute; left: 194px; top: 8px; }
  .status-time { position: absolute; left: 0; width: 640px; top: 7px; text-align: center; }
  .status-battery { position: absolute; right: 10px; top: 7px; display: flex; align-items: center; gap: 6px; }
  .battery { width: 46px; height: 22px; border: 2px solid var(--white); border-radius: 4px; padding: 2px; position: relative; }
  .battery::after { content: ""; position: absolute; right: -6px; top: 5px; width: 3px; height: 8px; background: var(--white); border-radius: 0 2px 2px 0; }
  .battery i { display: block; width: 100%; height: 100%; background: var(--white); border-radius: 1px; }
  .brand-name {
    position: absolute; left: 0; width: 640px; top: 56px; text-align: center;
    font-family: "Roboto", sans-serif; font-weight: 900; font-size: 40px; letter-spacing: 0.5px; line-height: 48px;
  }

  .feed { position: absolute; left: 18px; top: 149px; width: 604px; }
  .article-card {
    position: absolute; left: 0; width: 604px; height: 202px;
    background: var(--card-bg); border: 1px solid var(--card-border);
  }
  .topic-badge { position: absolute; left: 30px; top: 28px; width: 104px; text-align: center; }
  .topic-circle { width: 104px; height: 104px; border-radius: 50%; display: flex; align-items: center; justify-content: center; }
  .topic-label { display: block; margin-top: 10px; font-size: 25px; font-weight: 300; font-family: "Roboto", sans-serif; }
  .topic-heart .topic-circle { background: var(--heart-red); } .topic-heart .topic-label { color: var(--heart-red); }
  .topic-xray .topic-circle { background: var(--xray-orange); } .topic-xray .topic-label { color: var(--xray-orange); }
  .topic-health .topic-circle { background: var(--health-lime); } .topic-health .topic-label { color: var(--health-lime); }
  .topic-services .topic-circle { background: var(--services-blue); } .topic-services .topic-label { color: var(--services-blue); }
  .article-text { position: absolute; left: 168px; top: 26px; width: 414px; font-family: "Roboto Condensed", sans-serif; }
  .article-title { font-size: 29px; font-weight: 400; color: var(--title-ink); line-height: 38px; white-space: nowrap; }
  .article-summary {
    margin-top: 6px; font-size: 23.5px; font-weight: 300; color: var(--body-ink); line-height: 32.5px;
    text-align: justify; display: -webkit-box; -webkit-line-clamp: 3; -webkit-box-orient: vertical; overflow: hidden;
  }

  .tab-bar {
    position: absolute; left: 0; top: 1038px; width: 640px; height: 98px;
    background: #fbfbfb; border-top: 1px solid #cfcfcf; display: flex;
  }
  .tab { width: 160px; position: relative; color: var(--tab-ink); text-align: center; font-size: 19px; }
  .tab svg { position: absolute; left: 55px; top: 12px; }
  .tab-label { position: absolute; left: 0; width: 160px; top: 68px; }
  .tab-active { color: var(--tab-active); }
</style>
</head>
<body>
<div class="screen">
  <header class="app-header">
    <div class="status-bar">
      <div class="status-carrier">
        <div class="signal"><span class="on"></span><span class="on"></span><span class="on"></span><span></span><span></span></div>
        <span>Nexcell</span>
      </div>
      <svg class="wifi" width="26" height="20" viewBox="0 0 26 20" fill="none" stroke="#fff" stroke-width="2.6" stroke-linecap="round">
        <path d="M2 7a16 16 0 0 1 22 0"/><path d="M6 11a10 10 0 0 1 14 0"/><path d="M10 15a4.5 4.5 0 0 1 6 0"/>
      </svg>
      <div class="status-time">4:21 PM</div>
      <div class="status-battery"><span>100%</span><div class="battery"><i></i></div></div>
    </div>
    <div class="brand-name">Vorimelo</div>
  </header>

  <main class="feed">
    <article class="article-card" style="top:0">
      <div class="topic-badge topic-heart">
        <div class="topic-circle">
          <svg width="54" height="48" viewBox="0 0 54 48" fill="none" stroke="#fff" stroke-width="3" stroke-linejoin="round">
            <path d="M27 44 6 24A12 12 0 0 1 27 8a12 12 0 0 1 21 16Z"/>
          </svg>
        </div>
        <span class="topic-label">Heart</span>
      </div>
      <div class="article-text">
        <h2 class="article-title">5 Exercises to Improve Heart Health</h2>
        <p class="article-summary">You don’t need to be a hardcore athlete to boost your heart health. Moderate exercise can significantly reduce your risk of heart disease and stroke over time.</p>
      </div>
    </article>

    <article class="article-card" style="top:217px">
      <div class="topic-badge topic-xray">
        <div class="topic-circle">
          <svg width="46" height="56" viewBox="0 0 46 56" fill="none" stroke="#fff" stroke-width="2.5" stroke-linecap="round">
            <rect x="3" y="3" width="40" height="50" rx="3"/>
            <path d="M23 10v26M15 15h16M13 21h20M14 27h18M16 33h14"/>
            <path d="M15 40c3 6 13 6 16 0"/>
          </svg>
        </div>
        <span class="topic-label">X-ray</span>
      </div>
      <div class="article-text">
        <h2 class="article-title">How X-rays Work</h2>
        <p class="article-summary">As with many of mankind's monumental discoveries, X-ray technology was invented completely by accident. In 1895, a German physicist found a strange glow.</p>
      </div>
    </article>

    <article class="article-card" style="top:434px">
      <div class="topic-badge topic-health">
        <div class="topic-circle">
          <svg width="54" height="54" viewBox="0 0 54 54" fill="none" stroke="#fff" stroke-width="2.5" stroke-linecap="round" stroke-linejoin="round">
            <path d="M36 8l10 10M41 13l8-8M46 3l5 5"/>
            <path d="M38 16 14 40l-6-6 24-24Z"/>
            <path d="M11 37l-7 7M20 28l3 3M25 23l3 3"/>
          </svg>
        </div>
        <span class="topic-label">Health</span>
      </div>
      <div class="article-text">
        <h2 class="article-title">2-day Free Health Services</h2>
        <p class="article-summary">In connection with the National Health Month, the City of ABCDE will hold a week-long free health services to all of its residents this coming month.</p>
      </div>
    </article>

    <article class="article-card" style="top:651px">
      <div class="topic-badge topic-services">
        <div class="topic-circle">
          <svg width="56" height="48" viewBox="0 0 56 48" fill="none" stroke="#fff" stroke-width="2.5" stroke-linecap="round" stroke-linejoin="round">
            <path d="M4 14h30v22H4Z"/><path d="M34 20h10l8 8v8H34"/>
            <circle cx="13" cy="38" r="4"/><circle cx="43" cy="38" r="4"/>
            <path d="M19 19v12M13 25h12"/><path d="M22 2v5M14 5l3 4M30 5l-3 4"/>
          </svg>
        </div>
        <span class="topic-label">Services</span>
      </div>
      <div class="article-text">
        <h2 class="article-title">Sample T</h2>
        <p class="article-summary">In connection with the National Health Month, the City of ABCDE will hold a week-long free health services to all of its residents this coming month.</p>
      </div>
    </article>

    <article class="article-card" style="top:867px"></article>
  </main>

  <nav class="tab-bar">
    <div class="tab tab-active">
      <svg width="50" height="44" viewBox="0 0 50 44" fill="none" stroke="currentColor" stroke-width="2">
        <circle cx="5" cy="6" r="2.5"/><circle cx="5" cy="17" r="2.5"/><circle cx="5" cy="28" r="2.5"/><circle cx="5" cy="39" r="2.5"/>
        <path d="M13 6h32M13 17h32M13 28h32M13 39h32"/>
      </svg>
      <span class="tab-label">Feed</span>
    </div>
    <div class="tab">
      <svg width="50" height="52" viewBox="0 0 50 52" fill="none" stroke="currentColor" stroke-width="2" style="top:12px">
        <rect x="6" y="2" width="38" height="48" rx="2"/>
        <path d="M13 10h20M13 18h20M13 26h20M13 34h20M13 42h20"/>
        <circle cx="38" cy="10" r="1.5"/><circle cx="38" cy="18" r="1.5"/><circle cx="38" cy="26" r="1.5"/><circle cx="38" cy="34" r="1.5"/><circle cx="38" cy="42" r="1.5"/>
      </svg>
      <span class="tab-label">Topics</span>
    </div>
    <div class="tab">
      <svg width="50" height="50" viewBox="0 0 50 50" fill="none" stroke="currentColor" stroke-width="2">
        <circle cx="25" cy="25" r="23"/><circle cx="25" cy="20" r="6"/><path d="M14 33c0-5 22-5 22 0v2H14Z"/>
      </svg>
      <span class="tab-label">Profile</span>
    </div>
    <div class="tab">
      <svg width="50" height="44" viewBox="0 0 50 44" fill="none" stroke="currentColor" stroke-width="2">
        <circle cx="7" cy="26" r="5.5"/><circle cx="25" cy="26" r="5.5"/><circle cx="43" cy="26" r="5.5"/>
      </svg>
      <span class="tab-label">More</span>
    </div>
  </nav>
</div>
</body>
</html>
```